I need a business card design for my new clinic (SPORTS MEDICINE OF KNEE). I am orthopedist, expert in sports surgery, especially knee surgery. I prefer, as colors, the colors of my logo (green, black and white). I already have my logo and should appear on my card. It's good to see my site to have ideas (www.drlucianovarela.com)
It needs contain:
my name: Dr. Luciano Varela
my registration: CRM 584-902
my specialty: Cirurgia do Joelho / Esporte
my address: Centro Executivo - Pinheiral Plaza
Av. Doutor Augusto Brandão Cunha, 2740 sala 0836
Jd. Ipanema - Ribeirão Preto - SP
my phone number: Tel (16) 8245-3908
my clinic phone: (16) 3670-4851
my e-mail: drlucianovarela@mailbox-exemplo.com
my site: www.drlucianovarela.com

Target Market(s)

futures patients

Industry/Entity Type

Clinic

Requirements
Nice to have
• letters not overfilled
straight lines, with few curves

```html
<!DOCTYPE html>
<html lang="pt-BR">
<head>
<meta charset="utf-8">
<title>Dr. Luciano Varela — Cartão de visita</title>
<link rel="stylesheet" href="https://fonts.googleapis.com/css2?family=Arimo:wght@400;700&display=swap">
<style>
  :root {
    --frame: #1b1b1b;
    --page: #ffffff;
    --green: #35a55e;
    --green-light: #4cb16c;
    --card-light: #f7f7f7;
    --ink: #2b2b2b;
    --grey: #9a9a9a;
    --white: #ffffff;
  }
  * { margin: 0; padding: 0; box-sizing: border-box; }
  html, body {
    width: 1004px; height: 1200px; overflow: hidden;
    background: var(--page);
    font-family: "Arimo", Arial, sans-serif;
  }
  .presentation {
    position: relative;
    width: 1004px; height: 1200px;
    background: var(--frame);
    border-radius: 40px;
  }
  .card {
    position: absolute;
    left: 63px; width: 876px;
    overflow: hidden;
  }
  .card-front { top: 67px; height: 505px; background: var(--green); }
  .card-back { top: 625px; height: 507px; background: var(--card-light); }
  .card-shape { position: absolute; inset: 0; width: 100%; height: 100%; }

  .brand { position: absolute; display: flex; align-items: center; }
  .brand-square { display: block; border-radius: 8px; }
  .brand-name { font-weight: 400; line-height: 1; letter-spacing: 1px; }

  .card-front .brand { left: 207px; top: 195px; }
  .card-front .brand-square { width: 108px; height: 108px; background: var(--white); }
  .card-front .brand-name { margin-left: 24px; font-size: 80px; color: var(--white); }

  .website {
    position: absolute; left: 0; right: 0; top: 440px;
    text-align: center; color: var(--white);
    font-size: 23px; letter-spacing: 0.6px;
  }

  .card-back .brand { left: 49px; top: 210px; }
  .card-back .brand-square { width: 86px; height: 86px; background: var(--ink); }
  .card-back .brand-name { margin-left: 20px; font-size: 58px; color: var(--ink); }

  .contact {
    position: absolute; left: 476px; top: 86px;
    color: var(--ink); font-size: 17.5px; line-height: 27.5px;
  }
  .doctor-name { color: var(--green); font-size: 29px; line-height: 34px; margin-bottom: 1px; }
  .contact-group + .contact-group { margin-top: 17px; }
  .address + .phones { margin-top: 14px; }
</style>
</head>
<body>
<main class="presentation">

  <section class="card card-front">
    <svg class="card-shape" viewBox="0 0 876 505" preserveAspectRatio="none" aria-hidden="true">
      <path d="M0 0 H876 V97 C700 255 380 345 0 352 Z" fill="var(--green-light)"/>
    </svg>
    <div class="brand">
      <span class="brand-square"></span>
      <span class="brand-name">VARELA</span>
    </div>
    <p class="website">www.drlucianovarela.com</p>
  </section>

  <section class="card card-back">
    <svg class="card-shape" viewBox="0 0 876 507" preserveAspectRatio="none" aria-hidden="true">
      <path d="M0 437 C160 468 400 480 580 478 C400 492 160 500 0 505 Z" fill="var(--grey)"/>
      <path d="M876 412 C700 472 470 500 250 507 H876 Z" fill="var(--green)"/>
    </svg>
    <div class="brand">
      <span class="brand-square"></span>
      <span class="brand-name">VARELA</span>
    </div>
    <div class="contact">
      <div class="contact-group">
        <h1 class="doctor-name">Dr. Luciano Varela</h1>
        <p>CRM 584-902</p>
        <p>Cirurgia do Joelho / Esporte</p>
      </div>
      <div class="contact-group">
        <address class="address" style="font-style:normal">
          Centro Executivo - Pinheiral Plaza<br>
          Av. Doutor Augusto Brandão Cunha,<br>
          2740 sala 0836<br>
          Jd. Ipanema - Ribeirão Preto - SP
        </address>
        <div class="phones">
          <p>Telephone : (16) 8245-3908</p>
          <p>clinic phone : (16) 3670-4851</p>
          <p>e-mail: drlucianovarela@mailbox-exemplo.com</p>
        </div>
      </div>
    </div>
  </section>

</main>
</body>
</html>
```